Supplement Package and Bottle Design*

We are a supplement company rebranding a number of product ranges for which we need a designer.

We will start with two products for joint health supplementation that are part of one range.

1. DERMINOX K48 Internal Oil Drops
The internal oil drop requires a design for the outer box and inside bottle label – see attached.

Front of box should include the following text:
- DERMINOX K48
- Internal Oil Drops
- Original formula from the oils of fresh Laurus nobilis L. leaves and Curcuma longa L. rhizomes
- Dilute before use
- Food supplement
- 100ml
- Some prominent icon/ graphics indicating use for joint health
- Selunetra logo

2. DERMINOX R5 External Cream
The external cream only requires a design for the bottle label – see attached.
- DERMINOX R5
- External Cream
- Original formula from the oils of fresh Laurus nobilis L. leaves + 7 select ingredients
- 150ml
- Selunetra logo

Overall design:
- Common design between both products (oil drops and cream)
Must appeal to a customer base of middle-age/ seniors
- Pharmaceutical product feel with touch of nature/ herbal remedy
- Design my convey a feeling of dependability, trust, effectiveness
- Premium product feel. These are very expensive products
- Design must be easy to adapt for new product ranges
- Use icons/ symbols to indicate health application, example: icon of knee to indicate use for joints
- "K48" and "R5" should be prominent to distinguish the products
- You have a choice of two Selunetra logos. See attached.
- Primary colours: white and rgb(33, 136, 135)
- Designers can also consider some use of stamped gold/ silver for embellishments

Once a successful design/ feel has been chosen then exact dielines will be provided.

Target Market(s)

Seniors (65+ years old) with arthritis. Generally retired and affluent.

Industry/Entity Type

Health Product

Colors
33b8a4

Requirements
Must have
• As per project description.

Please creatively use a laurel wreath in the design. Either as a standalone element or multiple laurel wreaths in the background of the design. Can be vector or blended image.

As the supplements are made from bay leaves (laurel leaves) this subtle connection should be present.
Should not have
• Should not be cheap design and loud.

Premium design that conveys trust and pharmaceutical grade treatment with embellishments reminding that this is a natural/ herbal remedy product

```html
<!DOCTYPE html>
<html lang="en">
<head>
<meta charset="utf-8">
<title>Derminox K48 and R5 Packaging</title>
<link href="https://fonts.googleapis.com/css2?family=Montserrat:wght@600;700;800&family=Didact+Gothic&display=swap" rel="stylesheet">
<style>
  :root {
    --bg: #e4e5e5;
    --forest: #355e45;
    --sage: #6f9a86;
    --sage-light: #86ab99;
    --paper: #eceded;
    --white: #ffffff;
    --text: #3f4a44;
    --lid: #1f2120;
  }
  * { box-sizing: border-box; margin: 0; padding: 0; }
  html, body { width: 1200px; height: 800px; overflow: hidden; }
  body { background: var(--bg); font-family: "Didact Gothic", sans-serif; color: var(--text); position: relative; }
  .piece { position: absolute; overflow: hidden; }

  .brand { display: flex; flex-direction: column; align-items: center; gap: 10px; color: var(--forest); }
  .brand-dot { display: block; border: 3px solid var(--forest); border-radius: 50%; }
  .brand-name { display: block; letter-spacing: 0.24em; text-transform: uppercase; line-height: 1.2; }

  .product-name { font-family: "Montserrat", sans-serif; font-weight: 700; color: var(--forest); line-height: 1; text-align: center; }
  .product-code { font-family: "Montserrat", sans-serif; font-weight: 700; color: var(--forest); line-height: 0.9; text-align: center; letter-spacing: -0.02em; }

  .pill { position: relative; margin: 0 auto; background: var(--forest); color: var(--white); border-radius: 999px; text-align: center; font-family: "Montserrat", sans-serif; font-weight: 600; text-transform: uppercase; line-height: 1.2; }
  .pill::before, .pill::after { content: ""; position: absolute; top: 50%; height: 40%; transform: translateY(-50%); background: var(--forest); border-radius: 999px; }
  .pill::before { right: 100%; width: 18px; margin-right: -4px; }
  .pill::after { left: 100%; width: 18px; margin-left: -4px; }

  .formula { text-align: center; color: var(--text); }
  .badges { display: flex; justify-content: center; }
  .badge { display: block; border-radius: 50%; background: var(--sage); border: 3px solid var(--forest); box-shadow: inset 0 0 0 3px var(--white); }

  .band-dark { background: var(--forest); color: var(--white); text-align: center; font-family: "Montserrat", sans-serif; font-weight: 600; text-transform: uppercase; line-height: 1.2; }
  .band-sage { background: var(--sage); color: var(--white); text-align: center; }
  .band-sage .kind { font-family: "Montserrat", sans-serif; font-weight: 700; line-height: 1.2; }
  .band-sage .vol { line-height: 1.2; }

  /* Box front */
  .box-front { left: 90px; top: 80px; width: 290px; height: 640px; background: var(--paper); }
  .box-front .brand { margin-top: 28px; }
  .box-front .brand-dot { width: 78px; height: 78px; }
  .box-front .brand-name { font-size: 24px; }
  .box-front .product-name { font-size: 44px; margin-top: 16px; }
  .box-front .product-code { font-size: 118px; margin-top: 2px; }
  .box-front .pill { width: 210px; font-size: 15px; padding: 6px 0; margin-top: 10px; }
  .box-front .formula { font-size: 14.5px; line-height: 1.4; margin: 16px 22px 0; }
  .box-front .badges { gap: 8px; margin-top: 14px; }
  .box-front .badge { width: 52px; height: 52px; }
  .box-front .band-dark { position: absolute; left: 0; right: 0; top: 530px; font-size: 15px; padding: 6px 0; }
  .box-front .band-sage { position: absolute; left: 0; right: 0; top: 568px; bottom: 0; padding-top: 10px; }
  .box-front .band-sage .kind { font-size: 20px; }
  .box-front .band-sage .vol { font-size: 15px; margin-top: 6px; }

  /* Bottle label */
  .bottle-label { left: 420px; top: 175px; width: 300px; height: 330px; background: var(--white); }
  .bottle-label .brand { margin-top: 10px; gap: 5px; }
  .bottle-label .brand-dot { width: 44px; height: 44px; border-width: 2px; }
  .bottle-label .brand-name { font-size: 13px; }
  .bottle-label .product-name { font-size: 23px; margin-top: 8px; }
  .bottle-label .product-code { font-size: 58px; margin-top: 0; }
  .bottle-label .pill { width: 112px; font-size: 8px; padding: 3px 0; margin-top: 6px; }
  .bottle-label .pill::before, .bottle-label .pill::after { width: 10px; }
  .bottle-label .formula { font-size: 8px; line-height: 1.35; margin: 8px 40px 0; }
  .bottle-label .badges { gap: 6px; margin-top: 8px; }
  .bottle-label .badge { width: 30px; height: 30px; border-width: 2px; box-shadow: inset 0 0 0 2px var(--white); }
  .bottle-label .band-dark { position: absolute; left: 0; right: 0; top: 262px; font-size: 8px; padding: 3px 0; }
  .bottle-label .band-sage { position: absolute; left: 0; right: 0; top: 278px; bottom: 0; padding-top: 12px; }
  .bottle-label .band-sage .kind { font-size: 11px; }
  .bottle-label .band-sage .vol { font-size: 7px; margin-top: 3px; }

  /* Cream lid */
  .cream-lid { left: 815px; top: 90px; width: 270px; height: 270px; border-radius: 50%; background: var(--white); border: 14px solid var(--lid); }
  .cream-lid .inner { display: flex; flex-direction: column; align-items: center; padding-top: 34px; }
  .cream-lid .brand { gap: 6px; }
  .cream-lid .brand-dot { width: 42px; height: 42px; border-width: 2px; }
  .cream-lid .brand-name { font-size: 12px; }
  .cream-lid .product-name { font-size: 22px; margin-top: 8px; }
  .cream-lid .pill { width: 150px; font-size: 9px; padding: 3px 0; margin-top: 6px; }
  .cream-lid .vol { font-family: "Montserrat", sans-serif; font-weight: 600; font-size: 11px; margin-top: 6px; color: var(--text); }

  /* Cream side label */
  .cream-label { left: 760px; top: 430px; width: 380px; height: 200px; background: var(--white); display: flex; }
  .cream-label .edge-left { width: 40px; background: var(--sage); }
  .cream-label .badge-column { width: 44px; display: flex; flex-direction: column; justify-content: space-evenly; align-items: center; }
  .cream-label .badge { width: 28px; height: 28px; border-width: 2px; box-shadow: inset 0 0 0 2px var(--white); }
  .cream-label .front { flex: 1; display: flex; flex-direction: column; align-items: center; padding-top: 18px; }
  .cream-label .brand { gap: 5px; }
  .cream-label .brand-dot { width: 34px; height: 34px; border-width: 2px; }
  .cream-label .brand-name { font-size: 10px; }
  .cream-label .product-name { font-size: 22px; margin-top: 6px; }
  .cream-label .pill { width: 130px; font-size: 8px; padding: 3px 0; margin-top: 6px; }
  .cream-label .pill::before, .cream-label .pill::after { width: 10px; }
  .cream-label .formula { font-size: 7.5px; line-height: 1.35; margin: 8px 6px 0; }
  .cream-label .vol { font-family: "Montserrat", sans-serif; font-weight: 600; font-size: 8px; margin-top: 4px; }
  .cream-label .edge-right { width: 90px; background: var(--sage-light); border-top-left-radius: 60px 100px; border-bottom-left-radius: 60px 100px; color: var(--white); font-size: 6.5px; line-height: 1.45; padding: 30px 10px 0 22px; }
</style>
</head>
<body>

  <section class="piece box-front">
    <div class="brand">
      <span class="brand-dot"></span>
      <span class="brand-name">Selunetra</span>
    </div>
    <h1 class="product-name">DERMINOX</h1>
    <div class="product-code">K48</div>
    <div class="pill">Internal Oil Drops</div>
    <p class="formula">Original formula from the oils of fresh Laurus nobilis L. leaves and Curcuma longa L. rhizomes</p>
    <div class="badges">
      <span class="badge"></span><span class="badge"></span><span class="badge"></span><span class="badge"></span>
    </div>
    <div class="band-dark">Dilute before use</div>
    <div class="band-sage">
      <div class="kind">Food Supplement</div>
      <div class="vol">100ml</div>
    </div>
  </section>

  <section class="piece bottle-label">
    <div class="brand">
      <span class="brand-dot"></span>
      <span class="brand-name">Selunetra</span>
    </div>
    <h2 class="product-name">DERMINOX</h2>
    <div class="product-code">K48</div>
    <div class="pill">Internal Oil Drops</div>
    <p class="formula">Original formula from the oils of fresh Laurus nobilis L. leaves and Curcuma longa L. rhizomes</p>
    <div class="badges">
      <span class="badge"></span><span class="badge"></span><span class="badge"></span><span class="badge"></span>
    </div>
    <div class="band-dark">Dilute before use</div>
    <div class="band-sage">
      <div class="kind">Food Supplement</div>
      <div class="vol">100ml</div>
    </div>
  </section>

  <section class="piece cream-lid">
    <div class="inner">
      <div class="brand">
        <span class="brand-dot"></span>
        <span class="brand-name">Selunetra</span>
      </div>
      <h2 class="product-name">DERMINOX R5</h2>
      <div class="pill">External Cream</div>
      <div class="vol">150ml</div>
    </div>
  </section>

  <section class="piece cream-label">
    <div class="edge-left"></div>
    <div class="badge-column">
      <span class="badge"></span><span class="badge"></span><span class="badge"></span><span class="badge"></span>
    </div>
    <div class="front">
      <div class="brand">
        <span class="brand-dot"></span>
        <span class="brand-name">Selunetra</span>
      </div>
      <h2 class="product-name">DERMINOX R5</h2>
      <div class="pill">External Cream</div>
      <p class="formula">Original formula from the oils of fresh Laurus nobilis L. leaves + 7 select ingredients</p>
      <div class="vol">150ml</div>
    </div>
    <div class="edge-right">Apply a thin layer to the affected area two to three times daily and massage gently until absorbed. For external use only. Keep out of reach of children.</div>
  </section>

</body>
</html>
```